Web Concept Design - modernize website

Looking to modernize our current website. http :// hvkwmaplebrook . com

Color Scheme: Use uploaded palette. (Black, Silver, Dark Purple, Greyish Blue)

The website needs to have a patient-friendly, community-friendly feel to it. While still being a professional medical website. We don't want it to have a cold, clinical feel.

Information on home page needs to be split into their own separate pages with designs for each.

Home Page:
Lantern Walk-In & Family Care is a family practice and urgent care clinic dedicated to providing high quality, compassionate health care, to patients of all ages.
Hours of operation:
Monday-Friday 9am-6:30pm
Saturday: CLOSED
Sunday: CLOSED
Primary Care visits will be by appointment only.
We will accept our last new patient at 6:00p and our last established patient at 6:30p.
We will no longer be doing DOT Physicals.

At bottom of home page:

Lantern Walk-In & Family Care understands that information about your health is private and we know how important it is to keep your medical information protected. We follow all HIPAA guidelines to protect the privacy of your medical records. The privacy act below explains our privacy practices and how we may use and disclose your medical information. If you would like for Lantern Walk-In & Family Care to release any or all of your medical information to others, you can make the request by signing a release and bring it with you at your next visit. If you would like to contact someone about the privacy and/or use of your medical information, you may contact us at 205-318-7602.

Click here for HIPAA document.

Click here for Medical Release form.

---------------

Services Page:
We provide family and urgent care for patients of all ages.

-Annual physicals
-Pre-employment drug screening
-Women's care including pap smears
-Screening and treatment for diabetes, hypertension and cholesterol
-All minor trauma such as abscesses, lacerations, burns and fractures
-Minor skin complaints
-Onsite LAB/XRAY/EKG
-Weight loss
-Adult and Pediatric Vaccinations
-Osteopathic manual medicine
-Medical pain management

-----

Payment & Insurance Page:
We now have online bill pay for patient balances. Please visit https://secure.paynestclinic.com/lwfc382pay to pay your bill today!

We currently accept all forms of insurance with the exception of Medicaid. Please bring a copy of your insurance card and photo ID upon visit. We are also a Veltrix prime provider. We do accept self-pay for patients who do not have insurance.

----

Meet Our Providers Page:

Dr. Stephen (Steve) Hadley, DO
Family Practice Physician

Professional Experience
April 4, 2010 to Present Lantern Walk-In & Family Care Owner
12 years of Emergency Medicine experience
6/1994 - 7/1997 NMI Birmingham, AL
Family Medicine Residency
10/1997 to Present Board Certified in Family Medicine
Recertified 2004
Education
9/1990 to 5/1994 Fairhaven Institute of Osteopathic Studies
Old Westbury, New York
Degree: Doctor of Osteopathic Medicine
9/1985 to 5/1989 Carrow-Lindell College
Birmingham, Alabama
Degree: Bachelor of Science
Membership
National Guild of Household Clinicians
Physicians Council of the Gulf Territory

----

Navigation Bar should have links for all the above pages + NEW PATIENTS + Access Your Medical Records (feel free to be creative with how you design this). We don't want the navigation bar to be too crowded.

Target Market(s)

Medical Patients

Number of Pages Required

5+ page

Colors

Designer to choose colors to be used in the design.

Requirements
Must have
• Designs for all pages
• Keep it professional
Nice to have
• Be creative!
Should not have
• No cold clinical, medical websites

```html
<!DOCTYPE html>
<html lang="en">
<head>
<meta charset="utf-8">
<title>Lantern Walk-In &amp; Family Care</title>
<link rel="stylesheet" href="https://fonts.googleapis.com/css2?family=Open+Sans:ital,wght@0,400;0,600;0,700;1,400&display=swap">
<style>
:root{
  --teal:#4cc5cf;
  --teal-dark:#3b989f;
  --teal-pale:#eaf8f9;
  --ink:#333a3d;
  --muted:#8a9093;
  --red:#e8483b;
  --footer:#5f6062;
  --white:#ffffff;
  --map:#e8e9ea;
}
*{box-sizing:border-box;margin:0;padding:0}
html,body{width:1200px;height:2801px;overflow:hidden}
body{position:relative;font-family:"Open Sans",Arial,sans-serif;color:var(--ink);background:var(--white)}
.abs{position:absolute}

/* header */
.hero-photo{position:absolute;left:0;top:0;width:1200px;height:610px;
  background:radial-gradient(ellipse 420px 330px at 560px 250px,#b9d3dc 0%,#d6e6ec 45%,rgba(240,246,248,0) 100%),
  linear-gradient(180deg,#ffffff 0%,#f1f6f8 30%,#e1eef2 100%)}
.brand{left:86px;top:28px;display:flex;align-items:center;gap:12px}
.brand-dot{width:22px;height:22px;border-radius:50%;border:3px solid var(--teal)}
.brand-name{font-weight:700;font-size:19px;line-height:22px;color:var(--teal)}
.topbar{top:8px;left:700px;width:414px;display:flex;justify-content:space-between;align-items:center;font-size:10.5px}
.topbar .phone{color:var(--red);font-weight:600;font-size:13px;display:flex;gap:6px;align-items:center}
.topbar .addr{display:flex;gap:6px;align-items:center}
.nav{top:46px;left:612px;display:flex;gap:30px;font-size:11.5px;font-weight:600}
.nav a{color:var(--ink);text-decoration:none}
.nav a.current{color:var(--teal)}
.login{left:1036px;top:38px;width:78px;height:29px;border:2px solid var(--teal);color:var(--teal);font-size:11.5px;display:flex;align-items:center;justify-content:center}

/* hero */
.hero-title{left:145px;top:306px;font-size:38px;font-weight:600;color:#3a3f42;letter-spacing:-.2px}
.hero-lead{left:149px;top:368px;width:380px;font-size:14px;line-height:21px}
.hero-notes{left:149px;top:444px;font-size:9px;line-height:11px;color:var(--muted)}
.btn{background:var(--teal);color:var(--white);font-weight:600;display:flex;align-items:center;justify-content:center;text-align:center;box-shadow:0 3px 0 #3aa7b0}
.hero-btn{left:149px;top:494px;width:217px;height:44px;font-size:14px}
.hero-or{left:386px;top:504px;font-size:15px}
.hero-record{left:414px;top:505px;font-size:14px;border-bottom:1.5px solid var(--ink)}

/* info band */
.band{left:0;top:610px;width:776px;height:172px;background:var(--teal-dark);color:var(--white)}
.band-col{position:absolute;top:28px;font-size:12.5px;line-height:19px;font-weight:600}
.band-col hr{border:0;border-top:1.5px solid rgba(255,255,255,.7);width:120px;margin:8px 0 6px}
.band-link{display:flex;align-items:center;gap:12px;margin-top:10px;font-size:13.5px;font-weight:700}
.map-card{left:776px;top:517px;width:424px;height:336px;background:var(--map);box-shadow:0 6px 16px rgba(0,0,0,.25)}
.map-btn{left:146px;top:288px;width:130px;height:30px;font-size:13px;box-shadow:none}
.map-full{right:14px;top:296px;font-size:10px;color:#333}

/* services */
.sec-title{left:145px;font-size:29px;line-height:44px;font-weight:400;color:#333}
.sec-rule{height:3px;background:var(--muted);width:56px}
.svc-open{left:147px;top:1072px;font-size:15px;display:flex;align-items:center;gap:8px}
.tri-down{width:0;height:0;border-left:7px solid transparent;border-right:7px solid transparent;border-top:8px solid var(--teal)}
.tri-right{display:inline-block;width:0;height:0;border-top:7px solid transparent;border-bottom:7px solid transparent;border-left:8px solid var(--teal);margin-left:12px;vertical-align:-1px}
.svc-box{left:145px;top:1110px;width:910px;height:111px;background:var(--teal-pale)}
.svc-box p{position:absolute;left:24px;top:22px;width:560px;font-size:11.5px;line-height:18px;color:#555}
.svc-box-btn{left:645px;top:23px;width:236px;height:67px;font-size:14px;line-height:19px}
.svc-list{left:147px;top:1246px;list-style:none;font-size:15px}
.svc-list li{height:31.5px;line-height:22px}
.more{left:147px;top:1563px;font-size:15px;color:#2a8fa0;font-weight:600}

/* provider */
.video{left:145px;top:1765px;width:910px;height:509px;background:#1b1b1b}
.video-bar{position:absolute;left:0;top:0;width:100%;height:20px;font-size:10px;color:#eee;padding:4px 8px;background:#111}
.video-shot{position:absolute;left:0;top:20px;width:910px;height:465px;
  background:linear-gradient(90deg,#c9d3d6 0%,#e4e8e6 28%,#aab6bc 50%,#d9dcd8 75%,#b9c0c2 100%)}
.play{position:absolute;left:425px;top:217px;width:60px;height:40px;border-radius:8px;background:#1a1a1a;display:flex;align-items:center;justify-content:center}
.video-card{position:absolute;left:566px;top:340px;width:344px;height:138px;background:rgba(255,255,255,.9);padding:16px 20px;font-size:12px;line-height:16px;color:#333}
.video-ctrl{position:absolute;left:0;bottom:0;width:100%;height:24px;background:#222;border-top:3px solid #555}
.quote{left:300px;top:2330px;width:600px;text-align:center;font-style:italic;font-size:12.5px;line-height:28px;color:#a7acae}
.quote-name{left:300px;top:2390px;width:600px;text-align:center;font-size:12px;font-weight:600}
.badge{top:2427px;height:53px;background:#e6e8e9;border-radius:4px}
.foot-btn{left:492px;top:2520px;width:218px;height:44px;font-size:14px}

/* footer */
.footer{left:0;top:2636px;width:1200px;height:165px;background:var(--footer);border-top:4px solid var(--teal);color:var(--white)}
.top-btn{left:1093px;top:2620px;width:37px;height:42px;background:var(--teal);display:flex;align-items:center;justify-content:center}
.foot-brand{left:149px;top:54px;display:flex;align-items:center;gap:10px}
.foot-brand .brand-dot{border-color:var(--white);width:18px;height:18px;border-width:2px}
.foot-brand .brand-name{color:var(--white);font-size:13.5px;line-height:16px}
.copy{left:149px;top:114px;font-size:8.5px;color:#e5e5e5}
.foot-col{top:40px;font-size:12.5px;line-height:19px;font-weight:600}
.foot-col .label{font-weight:400;font-size:11px;color:#e0e0e0;margin-bottom:12px}
.foot-col .call{color:var(--red);font-size:17px;font-weight:700}
</style>
</head>
<body>

<div class="hero-photo" role="img" aria-label="Smiling team of clinic doctors and nurses in white coats and scrubs"></div>

<div class="abs brand"><span class="brand-dot"></span><span class="brand-name">Lantern Walk-In &amp;<br>Family Care</span></div>

<div class="abs topbar">
  <span class="addr"><svg width="10" height="13" viewBox="0 0 10 13"><path d="M5 0a5 5 0 0 0-5 5c0 3.5 5 8 5 8s5-4.5 5-8a5 5 0 0 0-5-5zm0 7a2 2 0 1 1 0-4 2 2 0 0 1 0 4z" fill="#333"/></svg>2180 Birchwell Avenue SUITE 204 MAPLEBROOK</span>
  <span class="phone"><svg width="13" height="13" viewBox="0 0 24 24"><path d="M6.6 10.8a15 15 0 0 0 6.6 6.6l2.2-2.2a1 1 0 0 1 1-.25 11.4 11.4 0 0 0 3.6.57 1 1 0 0 1 1 1V20a1 1 0 0 1-1 1A17 17 0 0 1 3 4a1 1 0 0 1 1-1h3.5a1 1 0 0 1 1 1c0 1.25.2 2.45.57 3.6a1 1 0 0 1-.25 1z" fill="#333"/></svg>205-318-7602</span>
</div>

<nav class="abs nav">
  <a class="current" href="#">Home</a><a href="#">Services</a><a href="#">Patient Resources</a><a href="#">Our Providers</a><a href="#">Contact</a>
</nav>
<div class="abs login">Login</div>

<h1 class="abs hero-title">High Quality &amp; Compassionate Health Care</h1>
<p class="abs hero-lead">Lantern Walk-In &amp; Family Care is a family practice and urgent care clinic dedicated to providing high quality, compassionate health care, to patients of all ages.</p>
<p class="abs hero-notes">* Primary Care visits will be by appointment only.<br>* We will no longer be doing DOT Physicals.</p>
<div class="abs btn hero-btn">Schedule My Appointment</div>
<span class="abs hero-or">or</span>
<span class="abs hero-record">Access My Record</span>

<section class="abs band">
  <div class="band-col" style="left:149px">
    <svg width="26" height="26" viewBox="0 0 26 26" style="margin-bottom:12px"><circle cx="13" cy="13" r="11" fill="none" stroke="#fff" stroke-width="2.5"/><path d="M13 6v7h5" fill="none" stroke="#fff" stroke-width="2.5"/></svg><br>
    Monday-Friday 9am-6:30pm<br>Saturday-SunDay: CLOSED
    <hr>
    New patient at 6:00pm<br>Established patient at 6:30pm.
  </div>
  <div class="band-col" style="left:477px">
    <svg width="20" height="26" viewBox="0 0 10 13" style="margin-bottom:12px"><path d="M5 0a5 5 0 0 0-5 5c0 3.5 5 8 5 8s5-4.5 5-8a5 5 0 0 0-5-5zm0 7a2 2 0 1 1 0-4 2 2 0 0 1 0 4z" fill="#fff"/></svg><br>
    2180 Birchwell Avenue<br>Suite 204<br>Maplebrook, AL 35198
    <div class="band-link">Get Direction <svg width="30" height="10" viewBox="0 0 30 10"><path d="M0 5h28M23 1l5 4-5 4" fill="none" stroke="#fff" stroke-width="1.5"/></svg></div>
  </div>
</section>

<div class="abs map-card">
  <div class="abs" style="inset:0;background:var(--map)" role="img" aria-label="Street map showing the clinic location"></div>
  <svg class="abs" style="left:186px;top:130px" width="24" height="30" viewBox="0 0 10 13"><path d="M5 0a5 5 0 0 0-5 5c0 3.5 5 8 5 8s5-4.5 5-8a5 5 0 0 0-5-5zm0 7a2 2 0 1 1 0-4 2 2 0 0 1 0 4z" fill="var(--teal)"/></svg>
  <div class="abs btn map-btn">Get Direction</div>
  <span class="abs map-full">Full Screen</span>
</div>

<h2 class="abs sec-title" style="top:930px">We Provide Family and Urgent<br>Care for Patients of All Ages.</h2>
<div class="abs sec-rule" style="left:147px;top:1012px"></div>

<div class="abs svc-open">Annual physicals <span class="tri-down"></span></div>
<div class="abs svc-box">
  <p>The general medical examination is a common form of preventive medicine involving visits to a general practitioner by well feeling adults on a regular basis. This is generally yearly or less frequently. It is known under various non-specific names, such as the periodic health evaluation, annual physical issues. We provide the best procedures &amp; treatment for this.</p>
  <div class="abs btn svc-box-btn">Schedule My Appointment<br>With Dr. Hadley</div>
</div>

<ul class="abs svc-list">
  <li>Pre-employment drug screening<span class="tri-right"></span></li>
  <li>Women's care including pap smears<span class="tri-right"></span></li>
  <li>Screening and treatment for diabetes, hypertension and cholesterol<span class="tri-right"></span></li>
  <li>All minor trauma such as abscesses, lacerations, burns and fractures<span class="tri-right"></span></li>
  <li>Minor skin complaints<span class="tri-right"></span></li>
  <li>Onsite LAB/XRAY/EKG<span class="tri-right"></span></li>
  <li>Weight loss<span class="tri-right"></span></li>
  <li>Adult and Pediatric Vaccinations<span class="tri-right"></span></li>
  <li>Osteopathic manual medicine<span class="tri-right"></span></li>
  <li>Medical pain management<span class="tri-right"></span></li>
</ul>
<span class="abs more">Load More Services</span>

<h2 class="abs sec-title" style="top:1662px">Meet Our Provider Dr. Stephen (Steve) Hadley</h2>
<div class="abs sec-rule" style="left:147px;top:1706px;width:84px;background:#333"></div>

<div class="abs video">
  <div class="video-bar">Urgent Care, Emergency Room or 911?</div>
  <div class="video-shot" role="img" aria-label="Video still of the family physician speaking in an exam room"></div>
  <div class="play"><svg width="18" height="20" viewBox="0 0 18 20"><path d="M0 0l18 10L0 20z" fill="#fff"/></svg></div>
  <div class="video-card">
    Dr. Stephen (Steve) Hadley, DO<br>Family Practice Physician<br><br>
    Membership:<br>National Guild of Household Clinicians<br>Physicians Council of the Gulf Territory
  </div>
  <div class="video-ctrl"></div>
</div>

<p class="abs quote">Just Walk in for urgent issues. I'm obliged to provide you with high quality and<br>affordable healthcare for everyone.</p>
<p class="abs quote-name">Dr. Stephen (Steve) Hadley, DO</p>
<div class="abs badge" style="left:418px;width:148px"></div>
<div class="abs badge" style="left:624px;width:292px"></div>

<div class="abs btn foot-btn">Schedule My Appointment</div>

<footer class="abs footer">
  <div class="abs foot-brand"><span class="brand-dot"></span><span class="brand-name">Lantern Walk-In &amp;<br>Family Care</span></div>
  <p class="abs copy">Copyright ©2012 Lantern Walk-In and Family Care, All rights reserved.</p>
  <div class="abs foot-col" style="left:496px"><div class="label">Location:</div>2180 Birchwell Avenue<br>Suite 204<br>Maplebrook, AL 35198</div>
  <div class="abs foot-col" style="left:702px"><div class="label">Hours:</div>Monday-Friday 9am-6:30pm<br>Saturday-SunDay: CLOSED</div>
  <div class="abs foot-col" style="left:940px"><div class="label">Call Us:</div><span class="call">205-318-7602</span></div>
</footer>
<div class="abs top-btn"><svg width="14" height="18" viewBox="0 0 14 18"><path d="M7 17V2M2 7l5-5 5 5" fill="none" stroke="#fff" stroke-width="2"/></svg></div>

</body>
</html>
```